"The Plum Principle" Book Cover Design

Name of book: The Plum Principle

Tagline: Exploring 8 essential truths to living and loving more deeply.

Author: Rosalinda Ferrando-Vega

Size: 5in w x 8in h Paperback

This is the second book of 30 year old Entrepreneur, Author and Speaker. The book basically tells the story of her youth and immigrating to the United States at 14.

"The Plum Principle" name came about since she started selling figs outside her home in mexico city... Her family had a fig three in their backyard, and when she was about 6 she had the courage of starting her own business.

Here is the Book Description:
At some point in our lives, we all face the question: Does crisis and pain propel us forward or put our lives on hold? In this deeply intimate memoir, Rosalinda Ferrando Vega shares the eight hidden secrets—the fig factors as she calls them—of discovering true awareness and embracing life’s big sky possibilities, even amidst our greatest struggles.

The Plum Principle is an emotionally-charged story spanning two countries and three decades. Vega expertly takes our hand and invites us to walk with her. We begin in her homeland of Mexico as she recounts her mother’s unrelenting faith in giving birth to a little girl, the good that came from the arsonist’s flames devouring her childhood home and the life-changing discovery she encountered after watching her father walk away again and again with a bottle in his hand. Her immigration to the United States as a young teenager and the amazing medical discovery that both saved her life while nearly taking it away offer true inspiration that the human spirit dictates triumph in the lives of everyday people.

Vega clearly touches our hearts in this beautifully written, very personal memoir, showing us how to find more to every moment of living through love, awareness, forgiveness, gratitude and more. Each chapter is capped off with thought-provoking questions underscoring Vega’ real message: the answers to life’s greatest questions lie within each of us.
Updates

The author's favorite colors are Purple, Lime Green, and Black...  notice that Figs are also purple

Target Market(s)

Mostly women but men should also get interested in reading book

Industry/Entity Type

Medical

Requirements
Must have
• Title, tagline, and author's name;

The Plum Principle

Unfolding the 8 hidden lessons for living and growing more fully

Rosalinda Ferrando-Vega

```html
<!DOCTYPE html>
<html lang="en">
<head>
<meta charset="utf-8">
<title>The Plum Principle — Book Cover</title>
<link rel="stylesheet" href="https://fonts.googleapis.com/css2?family=Cinzel:wght@400;500;600;700&display=swap">
<style>
  :root {
    --cream: #f6efcc;
    --plum-deep: #2e1f36;
    --fig-red: #d0204f;
    --fig-dark: #8e1238;
    --shadow: rgba(25, 12, 30, 0.6);
  }
  * { margin: 0; padding: 0; box-sizing: border-box; }
  html, body { width: 750px; height: 1200px; overflow: hidden; background: var(--plum-deep); }
  .cover {
    position: relative;
    width: 750px;
    height: 1200px;
    overflow: hidden;
    font-family: "Cinzel", "Times New Roman", serif;
    color: var(--cream);
    text-shadow: 0 2px 6px var(--shadow);
  }
  .cover-photo {
    position: absolute; inset: 0;
    background:
      radial-gradient(ellipse 40% 60% at 82% 45%, rgba(165,150,170,0.45), transparent 70%),
      radial-gradient(ellipse 38% 50% at 18% 28%, rgba(150,135,158,0.35), transparent 70%),
      linear-gradient(180deg, #4b3752 0%, #6d5a75 45%, #5b4763 75%, #3f2d47 100%);
  }
  .fig-cluster {
    position: absolute;
    left: 80px; top: 270px;
    width: 600px; height: 490px;
    border-radius: 46% 54% 44% 56% / 48% 46% 54% 52%;
    background: radial-gradient(circle at 42% 40%, #e0456f 0%, var(--fig-red) 40%, var(--fig-dark) 75%, transparent 90%);
  }
  .author {
    position: absolute; top: 68px; left: 0; right: 0;
    text-align: center;
    font-size: 36px; font-weight: 600; letter-spacing: 0.5px;
  }
  .title { font-weight: 500; }
  .title-line {
    position: absolute; left: 0; right: 0;
    text-align: center; line-height: 1;
  }
  .title-the { top: 258px; font-size: 155px; }
  .title-plum {
    top: 432px; font-size: 155px;
    display: flex; justify-content: center; align-items: center; gap: 14px;
  }
  .title-plum::before, .title-plum::after {
    content: ""; width: 46px; height: 10px;
    border-top: 2px solid var(--cream); border-bottom: 2px solid var(--cream);
  }
  .title-principle { top: 610px; font-size: 116px; }
  .tagline { font-weight: 700; }
  .tagline-row {
    position: absolute; left: 0; right: 0;
    text-align: center; line-height: 1;
  }
  .tagline-lead { top: 860px; font-size: 56px; }
  .tagline-mid { top: 937px; font-size: 50px; }
  .tagline-end { top: 1012px; font-size: 54px; }
  .tagline-last { top: 1094px; font-size: 38px; }
  .tagline-rule {
    position: absolute; height: 2px;
    background: var(--cream);
    box-shadow: 0 1px 4px var(--shadow);
  }
  .tagline-rule--one { top: 924px; left: 160px; width: 430px; }
  .tagline-rule--two { top: 999px; left: 170px; width: 410px; }
  .tagline-rule--three { top: 1075px; left: 170px; width: 410px; }
</style>
</head>
<body>
<main class="cover">
  <div class="cover-photo" role="img" aria-label="Muted purple photograph of a large tree trunk with twisting roots and leaves"></div>
  <div class="fig-cluster" role="img" aria-label="Cluster of ripe crimson plums with dark leaves"></div>

  <p class="author">Rosalinda Ferrando-Vega</p>

  <h1 class="title">
    <span class="title-line title-the">The</span>
    <span class="title-line title-plum">Plum</span>
    <span class="title-line title-principle">Principle</span>
  </h1>

  <p class="tagline">
    <span class="tagline-row tagline-lead">Unfolding the</span>
    <span class="tagline-row tagline-mid">8 hidden lessons</span>
    <span class="tagline-row tagline-end">for living and</span>
    <span class="tagline-row tagline-last">growing more fully</span>
  </p>
  <span class="tagline-rule tagline-rule--one"></span>
  <span class="tagline-rule tagline-rule--two"></span>
  <span class="tagline-rule tagline-rule--three"></span>
</main>
</body>
</html>
```